Brenmor Water - 500ml

to create a water bottle packaging similar to Brume Claire design. Bottle should be blue similar to NORTH KIND but change the design/logo to Brenmor. Wording should be similar just different design and logo. Thanks.

Colors
0054AA
0677BA
7BADD7
CADEEF
E8F1F8

Requirements
Must have
• Bottle must not be in plastic bottles. They are made in a carton instead - see NORTH KIND for reference.

```html
<!DOCTYPE html>
<html lang="en">
<head>
<meta charset="utf-8">
<title>Brenmor Water – Carton Dieline</title>
<link href="https://fonts.googleapis.com/css2?family=Baloo+2:wght@600;800&family=Montserrat:wght@400;600;700;800&display=swap" rel="stylesheet">
<style>
  :root{
    --navy:#0054AA;
    --blue:#0677BA;
    --sky:#7BADD7;
    --mist:#CADEEF;
    --ice:#E8F1F8;
    --white:#FFFFFF;
    --fold:#9AA8B6;
  }
  *{margin:0;padding:0;box-sizing:border-box}
  html,body{width:1200px;height:2336px;overflow:hidden;background:var(--white)}
  body{font-family:"Montserrat",sans-serif;position:relative}
  .dieline{position:absolute;left:0;top:488px;width:1200px;height:1360px}
  .dieline-art{position:absolute;inset:0}
  .panel{position:absolute;color:var(--white);text-align:center}
  .panel p{font-size:13px;line-height:1.35;margin-bottom:10px}
  .panel h3{font-weight:800;font-size:17px;line-height:1.2;margin-bottom:16px;letter-spacing:.02em}
  .on-white{color:var(--navy)}

  .panel--maker{left:14px;top:210px;width:162px;text-align:left}
  .panel--maker h3{font-size:16px;text-align:center}
  .panel--maker .lead{font-weight:700}
  .badge{display:block;width:70px;height:40px;background:var(--white);border-radius:4px;margin:14px 0 16px}
  .badge--round{width:54px;height:54px;border-radius:50%}
  .panel--cert{left:14px;top:1000px;width:162px;text-align:left}
  .panel--cert p{font-size:11px}

  .panel--claims{left:210px;top:220px;width:290px}
  .panel--claims p{font-size:14px;margin-bottom:22px}
  .claim-rule{width:40px;height:2px;background:var(--mist);margin:0 auto 22px}

  .brand{position:absolute;left:520px;top:150px;width:300px;text-align:center;color:var(--white)}
  .brand-name{font-family:"Baloo 2",sans-serif;font-weight:800;font-size:64px;line-height:1}
  .brand-tag{font-size:11px;letter-spacing:.08em;margin-top:4px;color:var(--ice)}
  .product-word{position:absolute;left:575px;top:300px;width:230px;height:540px;display:flex;align-items:center;justify-content:center}
  .product-word span{display:block;transform:rotate(90deg);font-family:"Baloo 2",sans-serif;font-weight:800;font-size:190px;color:var(--white);letter-spacing:.02em;line-height:1;white-space:nowrap}
  .front-foot{position:absolute;left:520px;top:968px;width:300px;text-align:center;color:var(--navy)}
  .front-foot .kind{font-weight:800;font-size:20px}
  .front-foot .desc{font-size:16px;line-height:1.3;margin-top:4px}
  .front-foot .vol{font-weight:700;font-size:18px;margin-top:4px}

  .panel--story{left:836px;top:220px;width:150px}
  .panel--story h3{font-size:17px}
  .panel--story p{font-size:12.5px}
  .panel--story .sign{font-weight:700;margin-top:14px}

  .panel--analysis{left:1000px;top:230px;width:186px;text-align:left}
  .panel--analysis h3{font-size:13px;margin-bottom:8px}
  .analysis{width:100%;border-collapse:collapse;font-size:11.5px;margin-bottom:18px}
  .analysis td{padding:3px 0;border-bottom:1px solid rgba(255,255,255,.45)}
  .analysis td:last-child{text-align:right;font-weight:700}
</style>
</head>
<body>
<main class="dieline">
  <svg class="dieline-art" width="1200" height="1360" viewBox="0 0 1200 1360">
    <defs>
      <linearGradient id="swirl" x1="0" y1="0" x2="1" y2="1">
        <stop offset="0" stop-color="#7BADD7"/>
        <stop offset=".45" stop-color="#0677BA"/>
        <stop offset="1" stop-color="#0054AA"/>
      </linearGradient>
    </defs>

    <g class="top-flaps" fill="#FFFFFF" stroke="#9AA8B6" stroke-width="2">
      <path d="M0 120 L0 60 L150 60 L190 120 Z"/>
      <path d="M190 120 L230 20 L480 20 L520 120 Z"/>
      <path d="M520 120 L560 60 L780 60 L820 120 Z"/>
      <path d="M820 120 L850 20 L950 20 L980 120 Z"/>
      <path d="M980 120 L1010 60 L1200 60 L1200 120 Z"/>
    </g>

    <rect class="swirl-field" role="img" aria-label="Blue flowing water swirl pattern" x="0" y="120" width="1200" height="800" fill="url(#swirl)"/>

    <path class="wave-band" d="M0 880 C120 840 220 920 340 880 S560 840 680 880 S900 920 1020 880 S1160 850 1200 870 L1200 1100 L0 1100 Z" fill="#7BADD7"/>
    <path class="wave-base" d="M0 900 C120 860 220 940 340 900 S560 860 680 900 S900 940 1020 900 S1160 870 1200 890 L1200 1100 L0 1100 Z" fill="#FFFFFF"/>

    <g class="bottom-flaps" fill="#FFFFFF" stroke="#9AA8B6" stroke-width="2">
      <rect x="0" y="1100" width="190" height="240"/>
      <rect x="190" y="1100" width="330" height="240"/>
      <rect x="520" y="1100" width="300" height="240"/>
      <rect x="820" y="1100" width="160" height="240"/>
      <rect x="980" y="1100" width="220" height="240"/>
      <path d="M190 1100 L355 1260 L520 1100 M355 1260 L355 1340 M820 1100 L900 1220 L980 1100 M900 1220 L900 1340" fill="none"/>
    </g>

    <g class="fold-lines" stroke="#9AA8B6" stroke-width="1.5" stroke-dasharray="8 6">
      <line x1="190" y1="120" x2="190" y2="1100"/>
      <line x1="520" y1="120" x2="520" y2="1100"/>
      <line x1="820" y1="120" x2="820" y2="1100"/>
      <line x1="980" y1="120" x2="980" y2="1100"/>
      <line x1="0" y1="120" x2="1200" y2="120"/>
      <line x1="0" y1="1100" x2="1200" y2="1100"/>
    </g>
  </svg>

  <section class="panel panel--maker">
    <h3>Produced &amp; Distributed by:<br>Brenmor Water</h3>
    <p><span class="lead">Spring water:</span> Collected from protected springs in the hills and filled close to source.</p>
    <p>For water quality information, visit brenmorwater.co</p>
    <span class="badge"></span>
    <span class="badge badge--round"></span>
  </section>
  <section class="panel panel--cert on-white">
    <p><strong>Mix</strong><br>Cartons from responsible sources and recycled fibres.</p>
  </section>

  <section class="panel panel--claims">
    <h3>GO AHEAD, JUDGE THE<br>DRINK BY ITS CARTON.</h3>
    <p>Our Water is From Simple Things</p>
    <div class="claim-rule"></div>
    <p>Natural Spring Water in a Carton Made from Plants</p>
    <div class="claim-rule"></div>
    <p>It's Free From Plastic</p>
    <div class="claim-rule"></div>
    <p>Sourcing Only Renewable Contents</p>
    <div class="claim-rule"></div>
    <p>All Trees Used Are Regrown</p>
    <div class="claim-rule"></div>
    <p>The Carton Keeps Water Fresh And Reduces Carbon Emissions</p>
  </section>

  <div class="brand">
    <div class="brand-name">Brenmor</div>
    <div class="brand-tag">SPRING WATER CO.</div>
  </div>
  <div class="product-word"><span>WATER</span></div>
  <div class="front-foot">
    <div class="kind">100% Spring Water</div>
    <div class="desc">Sustainably sourced water<br>in a plant based carton</div>
    <div class="vol">1L ℮</div>
  </div>

  <section class="panel panel--story">
    <h3>YOU JUST DID A GOOD THING</h3>
    <p>This carton is made mostly from plants, which means it's kinder to the planet than plastic.</p>
    <p>Start to finish, it's a better bottle.</p>
    <p>One carton might not save the world, but it's a start.</p>
    <p>So if you're going to buy packaged water, this one's better for everyone.</p>
    <p class="sign">BRENMOR WATER</p>
  </section>

  <section class="panel panel--analysis">
    <h3>TYPICAL WATER ANALYSIS (MG/L)</h3>
    <table class="analysis">
      <tr><td>Calcium</td><td>4.1</td></tr>
      <tr><td>Magnesium</td><td>2.3</td></tr>
      <tr><td>Sodium</td><td>9.0</td></tr>
      <tr><td>Potassium</td><td>0.8</td></tr>
      <tr><td>Bicarbonate</td><td>24</td></tr>
      <tr><td>pH</td><td>7.2</td></tr>
    </table>
    <h3>Packaging Facts</h3>
    <table class="analysis">
      <tr><td>Paper</td><td>75%</td></tr>
      <tr><td>Plant polymer</td><td>20%</td></tr>
      <tr><td>Aluminium</td><td>5%</td></tr>
    </table>
  </section>
</main>
</body>
</html>
```